Business Card Design

I am a RN and a Case Manager at a hospital. I would like some medical design

Industry/Entity Type

Medical

Contact Information for Business Card

Dorothy K Pendleford, BSN, RN/BA Sociology
Case Manager
Phone: Home 8174918267 Cell 8172639150

```html
<!DOCTYPE html>
<html lang="en">
<head>
<meta charset="UTF-8">
<title>Dorothy K Pendleford — Business Card</title>
<link rel="stylesheet" href="https://fonts.googleapis.com/css2?family=Fira+Sans:wght@400;700&display=swap">
<style>
  :root {
    --backdrop: #e9e9e6;
    --card-paper: #f5f3ec;
    --card-glow: #ffffff;
    --green: #4fae3f;
    --green-light: #9ad987;
    --green-pale: #cfe9c2;
    --band-text: #f2fbef;
  }
  * { box-sizing: border-box; margin: 0; padding: 0; }
  html, body {
    width: 1200px; height: 800px; overflow: hidden;
    background: var(--backdrop);
    font-family: "Fira Sans", Arial, sans-serif;
  }
  .business-card {
    position: absolute; left: 75px; top: 100px;
    width: 1050px; height: 600px;
    background: radial-gradient(ellipse at 60% 45%, var(--card-glow) 0%, var(--card-paper) 70%);
    overflow: hidden;
    box-shadow: 0 6px 24px rgba(0,0,0,.18);
  }
  .emblem-faint {
    position: absolute;
    background: radial-gradient(ellipse, var(--green-pale) 0%, rgba(207,233,194,0) 72%);
  }
  .emblem-faint--top { left: 40px; top: 10px; width: 220px; height: 250px; }
  .emblem-faint--side { left: 810px; top: 290px; width: 220px; height: 200px; }
  .nurse-mark {
    position: absolute; left: 360px; top: 30px;
    width: 170px; height: 225px;
    border-radius: 36px 36px 22px 22px;
    background: linear-gradient(180deg, var(--green-light) 0%, var(--green) 100%);
  }
  .band {
    position: absolute; left: 0; top: 0; width: 1050px; height: 600px;
  }
  .identity {
    position: absolute; left: 390px; top: 268px;
  }
  .identity__name {
    font-weight: 700; font-size: 40px; line-height: 48px; color: var(--green);
    letter-spacing: .5px; white-space: nowrap;
  }
  .identity__contact {
    margin-top: 8px; padding-left: 10px;
    font-size: 20px; line-height: 1.45; color: var(--green);
  }
  .credentials {
    position: absolute; left: 40px; top: 418px;
    font-size: 28px; color: var(--band-text); letter-spacing: 1px;
    white-space: nowrap;
    transform: rotate(7deg); transform-origin: left top;
  }
</style>
</head>
<body>
  <main class="business-card">
    <div class="emblem-faint emblem-faint--top" role="img" aria-label="Faint caduceus emblem"></div>
    <div class="emblem-faint emblem-faint--side" role="img" aria-label="Faint caduceus emblem, turned on its side"></div>

    <svg class="band" viewBox="0 0 1050 600" aria-hidden="true">
      <path d="M0 390 C 350 395, 700 480, 1050 575 L1050 600 L0 600 Z" fill="var(--green)"/>
      <path d="M0 380 C 350 385, 700 470, 1050 564" fill="none" stroke="var(--green-light)" stroke-width="3"/>
    </svg>

    <div class="nurse-mark" role="img" aria-label="Nurse figure in a capped hat with a stethoscope"></div>

    <section class="identity">
      <h1 class="identity__name">Dorothy K Pendleford</h1>
      <p class="identity__contact">Mobile: 817-263-9150<br>Phone: 817-491-8267</p>
    </section>

    <p class="credentials">BSN, RN/BA Sociology Case Manager</p>
  </main>
</body>
</html>
```